パック詰めしたカニ身を入れる袋のデザインを依頼させていただきます。中の商品が見えるように、また通販のお客様だけでなく、デパートの食品売り場や高級スーパーで手にとっていただけるような、高級感のあるデザイン案をお願いします。イメージは『和モダン』です。
▼デザインの仕様▼
【袋サイズ】W200×H300(mm)
【デザインしていただく部分】W200×H270(mm)
※袋下30mmは空けておいてください。
商品が入った状態の参考画像は添付ファイル①を参照
(今回は袋のデザインをお願いします)
【色の数】4色まで
【材質】PP

▼記載内容▼※文字サイズ、字体、配置はおまかせいたします。
【商品名】右記よりどれか(かに身 ・ カニ身 ・ 蟹身)
【会社名】南浜商店
【賞味期限印刷用スペース】W30×H10(mm)※白抜きで
【商品特長】以下よりいくつか選択の上記載してください。
※表現は自由に変更してください。
・茹でへのこだわり(アルカリ水、瀬波の白粒使用)
・兵庫 香住港産
・日本海の深層水で育まれた
・みずみずしい
・カニ本来の甘み
【イメージ画像】添付ファイル②参照
※こちらは使っていただいてもいただかなくてもどちらでも結構です。
赤系、グレー系、黒・ゴールド等、高級感のある色
• 高解像度JPG (.jpg)
• イラストレーター形式 (.ai)
参考画像追記しておきます
多くのご提案ありがとうございます。
ご検討いただいているランサーの皆様に弊社よりお願いがあります。

1.依頼開始当初より記載しておりました、『和モダン』というイメージにあまり固執されすぎることなく、各ランサー様の自由な発想でデザインしていただきたい。
2.添付ファイル②のカニの画像は使用しないでください。

大変申し訳ございませんが、既にご提案いただいております皆様も、上記の点を踏まえまして、再度のご検討、ご提案いただければと思います。
残り日数少ない中、急な変更ではございますが何卒宜しくお願い致します。
上記変更に伴い、締め切りを1日延長させていただきます。
よろしくお願いいたします

ご質問等ございましたら、お気軽にお問い合わせ下さい。

・伝えたいことを見ただけで分かりやすくとらえることができる。
・主張しすぎないデザインの中に、高級感、上品さが感じ取れる。
・バランスがよく、中のカニ身を引き立ててくれると感じた。

皆様の貴重なお時間を、弊社依頼に費やしていただきまして、誠にありがとうございました。
今回見送らせていただいた皆様のご提案の中にも、素晴らしいデザインのものが数多くありました。今後もTesmora内におきまして他製品のパッケージやパンフレット等の依頼ができればと思っております。その際は是非また、素敵なご提案をお願いいたします。

```html
<!DOCTYPE html>
<html lang="ja">
<head>
<meta charset="utf-8">
<title>かに身 パッケージ</title>
<link rel="stylesheet" href="https://fonts.googleapis.com/css2?family=Shippori+Mincho:wght@500;700;800&family=Noto+Serif+JP:wght@600;900&display=swap">
<style>
  :root {
    --bag-red: #c8141c;
    --bag-red-deep: #a10c14;
    --title-red: #d5161e;
    --ink: #1a1010;
    --gold: #d9b45a;
    --gold-deep: #8a5f14;
    --white: #ffffff;
    --tray: #141414;
    --meat-light: #f6ece2;
    --meat-pink: #e9a99a;
  }
  * { margin: 0; padding: 0; box-sizing: border-box; }
  html, body { width: 849px; height: 1200px; overflow: hidden; background: #fff; }
  .package {
    position: relative;
    width: 849px; height: 1200px;
    background: radial-gradient(ellipse at 50% 40%, var(--bag-red) 0%, var(--bag-red-deep) 100%);
    overflow: hidden;
    font-family: "Shippori Mincho", serif;
  }
  .product-window {
    position: absolute;
    left: 82px; top: 46px; width: 730px; height: 1070px;
    border-radius: 44px;
    background: linear-gradient(180deg, #fbf6f1 0%, var(--meat-light) 45%, #f1cdbf 70%, var(--meat-pink) 100%);
  }
  .crab-illustration {
    position: absolute;
    left: 52px; top: 14px; width: 170px; height: 165px;
    border-radius: 50%;
    background: radial-gradient(circle, #e07a4a 0%, #c8542e 60%, rgba(200,84,46,0) 100%);
  }
  .title-plate {
    position: absolute;
    left: 40px; top: 360px; width: 240px; height: 132px;
    background: var(--title-red);
    box-shadow: 0 3px 8px rgba(0,0,0,.35);
    text-align: center;
    color: var(--white);
  }
  .title-plate .product-name {
    font-family: "Noto Serif JP", serif;
    font-weight: 900;
    font-size: 72px;
    line-height: 1;
    padding-top: 14px;
    letter-spacing: 2px;
  }
  .title-plate .variety {
    font-family: "Shippori Mincho", serif;
    font-weight: 700;
    font-size: 20px;
    margin-top: 10px;
    letter-spacing: 2px;
  }
  .romaji {
    position: absolute;
    left: 44px; top: 498px;
    font-family: "Shippori Mincho", serif;
    font-weight: 700;
    font-size: 30px;
    color: var(--gold);
    text-shadow: 0 1px 2px rgba(80,30,0,.35);
  }
  .features {
    position: absolute;
    left: 400px; top: 100px; height: 560px; width: 420px;
    writing-mode: vertical-rl;
    font-family: "Shippori Mincho", serif;
    font-weight: 800;
    font-size: 35px;
    line-height: 1.88;
    color: var(--ink);
    letter-spacing: 1px;
  }
  .maker {
    position: absolute;
    left: 690px; top: 622px;
    display: flex; align-items: center; gap: 6px;
    font-family: "Shippori Mincho", serif;
    font-weight: 700;
    font-size: 19px;
    color: var(--ink);
  }
  .maker .seal { width: 18px; height: 18px; background: var(--title-red); }
  .net-weight {
    position: absolute;
    left: 412px; top: 1070px;
    font-family: "Shippori Mincho", serif;
    font-weight: 800;
    font-size: 28px;
    color: var(--gold-deep);
  }
  .expiry-box {
    position: absolute;
    left: 652px; top: 1062px; width: 155px; height: 42px;
    background: var(--white);
    border: 1px solid #999;
    font-size: 12px;
    padding: 3px 5px;
    color: var(--ink);
  }
  .tray-base {
    position: absolute;
    left: 0; bottom: 0; width: 849px; height: 82px;
    background: var(--tray);
  }
</style>
</head>
<body>
  <div class="package">
    <div class="product-window" role="img" aria-label="袋の窓から見える紅ズワイガニの棒肉"></div>
    <div class="crab-illustration" role="img" aria-label="赤いカニのイラスト"></div>

    <div class="title-plate">
      <div class="product-name">かに身</div>
      <div class="variety">紅ズワイガニ</div>
    </div>
    <div class="romaji">Beni Zuwai Gani</div>

    <p class="features">兵庫県香住港産<br>日本海の深層水生まれ<br>兵庫県瀬波の白粒と<br>アルカリ水で茹であげ<br>かに本来のうまみを引き出した<br>みずみずしいおいしさ。</p>

    <div class="maker"><span>南浜商店</span><span class="seal"></span></div>

    <div class="net-weight">500g入</div>
    <div class="expiry-box">賞味期限</div>

    <div class="tray-base"></div>
  </div>
</body>
</html>
```